Real Estate Managemene Company Needs Business Card Design

We have a logo design and just need business cards made now for our business. Please use PDF logo # 3.

Card with Information to be attached shortly.

The card is used for a real estate management company. We will need to add four other employees and their cards.

Industry/Entity Type

Real Estate

Contact Information for Business Card

Tariq Hamdan
President
3187 Thornwick Avenue
Suite C
Glendale Heights, IL 60152
Phone 630.417.2286
Fax 630.417.2287
Cell 630.473.8062
vantorp@mailbreeze.net

Once design is approved we will have four other employees
Omar Hamdan
Operations Manager

Nadia Hamdan
Administrative Manager

Faz Hamdan
Principal

We would need to take out the cell # 630.473.8062 out for the remaining three cards.

Requirements
Must have
• Please use logo attached

```html
<!DOCTYPE html>
<html lang="en">
<head>
<meta charset="utf-8">
<title>Northgate Property Management Group – Business Card</title>
<link href="https://fonts.googleapis.com/css2?family=Cinzel:wght@400;600&family=Crimson+Text&family=Lato:wght@700&display=swap" rel="stylesheet">
<style>
  :root {
    --backdrop: #2b2b2b;
    --card: #f4f4f4;
    --navy: #1c4a7d;
    --ink: #1e1e1e;
    --muted: #3a3a3a;
    --band-text: #dce6f2;
  }
  html, body {
    margin: 0;
    width: 1200px;
    height: 873px;
    overflow: hidden;
    background: var(--backdrop);
  }
  .card {
    position: absolute;
    left: 150px;
    top: 180px;
    width: 900px;
    height: 514px;
    background: var(--card);
    overflow: hidden;
    box-shadow: 0 18px 40px rgba(0,0,0,.55);
  }
  .brand {
    position: absolute;
    top: 96px;
    left: 0;
    width: 100%;
    text-align: center;
    font-family: "Cinzel", serif;
    font-weight: 600;
    color: var(--navy);
  }
  .brand-mark {
    display: inline-block;
    width: 26px;
    height: 26px;
    background: var(--navy);
    margin-bottom: 8px;
  }
  .brand-name {
    font-size: 52px;
    line-height: 1;
    letter-spacing: 1px;
  }
  .brand-tag {
    font-size: 15px;
    margin-top: 4px;
    letter-spacing: 1px;
  }
  .person {
    position: absolute;
    right: 575px;
    top: 268px;
    text-align: right;
    white-space: nowrap;
  }
  .person-name {
    font-family: "Cinzel", serif;
    font-size: 30px;
    line-height: 1.2;
    color: var(--navy);
  }
  .person-title {
    font-family: "Crimson Text", serif;
    font-size: 19px;
    color: var(--ink);
  }
  .divider {
    position: absolute;
    left: 345px;
    top: 256px;
    width: 2px;
    height: 88px;
    background: linear-gradient(var(--navy), rgba(28,74,125,0));
  }
  .contact {
    position: absolute;
    top: 250px;
    list-style: none;
    margin: 0;
    padding: 0;
    font-family: "Crimson Text", serif;
    font-size: 19px;
    color: var(--muted);
    white-space: nowrap;
  }
  .contact li {
    display: flex;
    align-items: center;
    gap: 10px;
    height: 34px;
  }
  .contact svg { width: 20px; height: 20px; fill: var(--navy); }
  .contact-office { left: 385px; }
  .contact-mobile { left: 600px; }
  .skyline {
    position: absolute;
    left: 0;
    bottom: 0;
    width: 900px;
    height: 230px;
  }
  .address {
    position: absolute;
    left: 0;
    bottom: 26px;
    width: 100%;
    text-align: center;
    font-family: "Lato", sans-serif;
    font-weight: 700;
    font-size: 19px;
    color: var(--band-text);
  }
</style>
</head>
<body>
  <div class="card">
    <div class="brand">
      <span class="brand-mark"></span>
      <div class="brand-name">Northgate</div>
      <div class="brand-tag">Property Management Group</div>
    </div>

    <div class="person">
      <div class="person-name">Tariq Hamdan</div>
      <div class="person-title">President</div>
    </div>

    <div class="divider"></div>

    <ul class="contact contact-office">
      <li>
        <svg viewBox="0 0 24 24"><path d="M3 9c0-3 4-5 9-5s9 2 9 5v2h-5V9H8v2H3zM6 12h12l2 8H4z"/></svg>
        555.417.2286
      </li>
      <li>
        <svg viewBox="0 0 24 24"><path d="M7 3h10v5H7zM3 9h18v8h-4v4H7v-4H3zM9 15v4h6v-4z"/></svg>
        555.417.2287
      </li>
    </ul>

    <ul class="contact contact-mobile">
      <li>
        <svg viewBox="0 0 24 24"><path d="M7 2h10a1 1 0 0 1 1 1v18a1 1 0 0 1-1 1H7a1 1 0 0 1-1-1V3a1 1 0 0 1 1-1zm1 3v13h8V5z"/></svg>
        555.473.8062
      </li>
      <li>
        <svg viewBox="0 0 24 24"><path d="M2 5h20v14H2zm2 2v.5l8 5.5 8-5.5V7zm0 3v7h16v-7l-8 5.5z"/></svg>
        vantorp@mailbreeze.net
      </li>
    </ul>

    <svg class="skyline" viewBox="0 0 900 230" preserveAspectRatio="none" role="img" aria-label="City skyline silhouette rising toward the right">
      <defs>
        <linearGradient id="band" x1="0" y1="0" x2="0" y2="1">
          <stop offset="0" stop-color="#1f4f85"/>
          <stop offset="1" stop-color="#173f6b"/>
        </linearGradient>
      </defs>
      <polygon points="0,170 900,70 900,230 0,230" fill="url(#band)"/>
    </svg>

    <div class="address">3187 Thornwick Avenue Suite C, Ashford Springs, OH 44187</div>
  </div>
</body>
</html>
```